Willow Crest Mind Studio

I need a brain fitness website that is on the WordPress platform. It needs to feel friendly and relaxing. We are not a physical health gym, but a brain health coaching facility. I can produce hundreds of professional photos. It can be one long page or five short pages.

Industry/Entity Type

Health And Wellness

```html
<!DOCTYPE html>
<html lang="en">
<head>
<meta charset="utf-8">
<title>Willow Crest Mind Studio — Brain Coaching &amp; Fitness</title>
<link href="https://fonts.googleapis.com/css2?family=Roboto:ital,wght@0,400;0,500;0,700;1,400&family=Open+Sans:ital,wght@0,400;0,600;1,400&display=swap" rel="stylesheet">
<style>
  :root {
    --plum: #a3195b;
    --plum-dark: #8a1550;
    --teal: #1d5c80;
    --navy: #0e3652;
    --navy-deep: #0a2639;
    --sky: #2fa3d3;
    --heading: #1f5378;
    --text: #7a7a7a;
    --ink: #222;
    --white: #fff;
    --line: #d9d9d9;
  }
  * { box-sizing: border-box; margin: 0; padding: 0; }
  html, body { width: 1200px; height: 3416px; overflow: hidden; }
  body { position: relative; background: var(--white); font-family: "Open Sans", Arial, sans-serif; color: var(--text); }
  .abs { position: absolute; }

  /* Header */
  .site-header { position: absolute; left: 0; top: 0; width: 1200px; height: 109px; background: var(--white); }
  .brand { position: absolute; left: 118px; top: 30px; display: flex; align-items: center; gap: 14px; }
  .brand-dot { width: 48px; height: 48px; border-radius: 50%; background: var(--plum); flex: none; }
  .brand-name { font-family: "Roboto", Arial, sans-serif; font-weight: 500; font-size: 18px; color: var(--plum); letter-spacing: 0.5px; text-transform: uppercase; white-space: nowrap; }
  .main-nav { position: absolute; left: 524px; top: 50px; width: 564px; display: flex; justify-content: space-between; font-family: "Roboto", Arial, sans-serif; font-size: 14px; font-weight: 500; color: var(--ink); white-space: nowrap; }
  .main-nav .active { color: var(--sky); }

  /* Hero */
  .hero { position: absolute; left: 0; top: 109px; width: 1200px; height: 680px; overflow: hidden;
    background: radial-gradient(ellipse 420px 330px at 600px 300px, #3a5e96 0%, #1a2a4d 45%, #05070d 80%, #000 100%); }
  .hero-play { position: absolute; left: 548px; top: 158px; width: 104px; height: 104px; border: 5px solid var(--white); border-radius: 50%; }
  .hero-title { position: absolute; left: 0; top: 287px; width: 1200px; text-align: center; font-family: "Roboto", Arial, sans-serif; font-weight: 700; font-size: 52px; color: var(--white); letter-spacing: 0.5px; }
  .hero-sub { position: absolute; left: 0; top: 360px; width: 1200px; text-align: center; font-family: "Roboto", Arial, sans-serif; font-weight: 700; font-size: 31px; color: var(--white); text-transform: uppercase; }
  .hero-curve { position: absolute; left: 0; bottom: 0; }

  /* About */
  .section-title { position: absolute; left: 0; width: 1200px; text-align: center; font-family: "Roboto", Arial, sans-serif; font-weight: 500; text-transform: uppercase; }
  .about-title { top: 804px; font-size: 33px; color: var(--heading); }
  .about-copy { position: absolute; left: 214px; top: 866px; width: 772px; text-align: center; font-size: 14.5px; line-height: 26px; }
  .about-copy p + p { margin-top: 12px; }
  .brain-visual { position: absolute; left: 387px; top: 1030px; width: 390px; height: 329px;
    background: linear-gradient(180deg, #f7e3e5 0%, #f0c9cd 100%); }
  .feature-label { position: absolute; font-family: "Roboto", Arial, sans-serif; font-weight: 700; font-size: 14px; color: var(--ink); text-transform: uppercase; line-height: 18px; }
  .feature-lines { position: absolute; left: 0; top: 1080px; }

  /* Services */
  .services { position: absolute; left: 0; top: 1359px; width: 1200px; height: 452px;
    background: linear-gradient(110deg, var(--teal) 0%, #2a5a7e 35%, #7a2a63 70%, var(--plum) 100%); }
  .services .section-title { top: 54px; font-size: 28px; color: var(--white); }
  .service { position: absolute; top: 134px; width: 236px; text-align: center; color: var(--white); }
  .service-icon { width: 110px; height: 110px; margin: 0 auto; border: 2px solid var(--white); border-radius: 50%; display: flex; align-items: center; justify-content: center; }
  .service h3 { margin-top: 32px; font-family: "Roboto", Arial, sans-serif; font-weight: 700; font-size: 17px; text-transform: uppercase; }
  .service p { margin-top: 10px; font-size: 11px; line-height: 18px; padding: 0 14px; }

  /* Testimonials */
  .testimonials { position: absolute; left: 0; top: 1811px; width: 1200px; height: 416px;
    background: linear-gradient(90deg, #2186b8 0%, #3aa6d2 45%, #5cb8de 60%, #2d9fd0 100%); }
  .testimonials .section-title { top: 58px; font-size: 27px; color: var(--white); }
  .quote-mark { position: absolute; left: 0; top: 118px; width: 1200px; text-align: center; font-family: "Roboto", Arial, sans-serif; font-weight: 700; font-size: 76px; color: var(--white); line-height: 1; }
  .quote-text { position: absolute; left: 262px; top: 196px; width: 676px; text-align: center; font-style: italic; font-size: 15px; line-height: 25px; color: var(--white); }
  .quote-author { position: absolute; left: 0; top: 282px; width: 1200px; text-align: center; font-family: "Roboto", Arial, sans-serif; font-size: 14px; color: var(--white); text-transform: uppercase; }
  .quote-rule { position: absolute; left: 580px; top: 311px; width: 40px; height: 2px; background: var(--white); }

  /* Blogs */
  .blogs-title { top: 2284px; font-size: 27px; color: var(--heading); }
  .blog-card { position: absolute; border: 1px solid var(--line); background: var(--white); }
  .blog-media { position: absolute; }
  .blog-card h4 { position: absolute; font-family: "Roboto", Arial, sans-serif; font-weight: 400; font-size: 16px; color: #333; }
  .blog-card p { position: absolute; font-size: 10.5px; line-height: 16px; color: var(--text); }
  .btn-read { position: absolute; height: 32px; width: 118px; background: var(--plum); color: var(--white); font-family: "Roboto", Arial, sans-serif; font-size: 12px; font-weight: 500; text-transform: uppercase; display: flex; align-items: center; justify-content: center; }

  /* Contact */
  .contact { position: absolute; left: 0; top: 2819px; width: 1200px; height: 512px;
    background: radial-gradient(ellipse 700px 400px at 80% 40%, #1c5d7d 0%, var(--navy) 55%, #0a2a42 100%); }
  .contact .section-title { top: 52px; font-size: 26px; color: var(--white); }
  .contact-rule { position: absolute; left: 548px; top: 92px; width: 104px; height: 2px; background: var(--white); }
  .contact-info { position: absolute; left: 0; top: 128px; width: 1200px; display: flex; justify-content: center; gap: 42px; font-size: 14px; color: var(--white); }
  .contact-item { display: flex; align-items: center; gap: 12px; }
  .contact-icon { width: 34px; height: 34px; border-radius: 50%; background: var(--plum); display: flex; align-items: center; justify-content: center; }
  .field { position: absolute; height: 36px; border: 1px solid #9fb6c6; background: rgba(10,30,48,0.55); color: var(--white); font-size: 12px; padding: 10px 12px; }
  .field-message { height: 98px; }
  .btn-submit { position: absolute; left: 483px; top: 442px; width: 191px; height: 40px; background: var(--plum); color: var(--white); font-family: "Roboto", Arial, sans-serif; font-weight: 500; font-size: 15px; text-transform: uppercase; display: flex; align-items: center; justify-content: center; }

  .site-footer { position: absolute; left: 0; top: 3331px; width: 1200px; height: 85px; background: var(--navy-deep); color: #9fb3c2; font-size: 12px; text-align: center; line-height: 85px; }
</style>
</head>
<body>

<header class="site-header">
  <div class="brand">
    <span class="brand-dot"></span>
    <span class="brand-name">Willow Crest Mind Studio</span>
  </div>
  <nav class="main-nav">
    <span class="active">HOME</span><span>ABOUT US</span><span>SERVICES</span><span>TESTIMONIAL</span><span>BLOG</span><span>CONTACT</span>
  </nav>
</header>

<section class="hero" role="img" aria-label="Glowing network of connected points forming a human brain on a dark background">
  <div class="hero-play">
    <svg width="94" height="94" viewBox="0 0 94 94"><path d="M38 30 L64 47 L38 64 Z" fill="#fff"/></svg>
  </div>
  <h1 class="hero-title">BRAIN COACHING &amp; FITNESS</h1>
  <p class="hero-sub">Fusce ultricies orci ac feugiat</p>
  <svg class="hero-curve" width="1200" height="110" viewBox="0 0 1200 110">
    <path d="M0 110 L0 70 Q600 -10 1200 70 L1200 110 Z" fill="#fff"/>
    <path d="M0 70 Q600 -10 1200 70" fill="none" stroke="#a3195b" stroke-width="6"/>
  </svg>
</section>

<h2 class="section-title about-title">About Willow Crest</h2>
<div class="about-copy">
  <p>commodo a mi Morbi ornare gravida elit Integer congue augue et malesuada iaculis ipsum dui aliquet felis at cursus magna nisl nec elit Praesent elementum elit at tellus nec ultricies sit amet</p>
  <p>porttitor mattis enim In massa libero interdum nec interdum vel blandit sed nulla In ullamcorper est eget tempor cursus neque mi consectetuer mi a ultricies massa est sed nisl Class aptent taciti sociosqu ad litora torquent per conubia nostra per inceptos hymenaeos Proin nulla arcu</p>
</div>

<div class="brain-visual" role="img" aria-label="Photo of a pink anatomical model of a human brain"></div>
<svg class="feature-lines" width="1200" height="180" viewBox="0 0 1200 180">
  <g stroke="#1f5378" stroke-width="2" fill="#1f5378">
    <line x1="292" y1="36" x2="387" y2="36"/><circle cx="292" cy="36" r="4"/>
    <line x1="777" y1="36" x2="912" y2="36"/><circle cx="912" cy="36" r="4"/>
    <line x1="292" y1="150" x2="387" y2="150"/><circle cx="292" cy="150" r="4"/>
    <line x1="777" y1="150" x2="912" y2="150"/><circle cx="912" cy="150" r="4"/>
  </g>
</svg>
<div class="feature-label" style="left:196px; top:1096px; text-align:center;">Experience<br>Member</div>
<div class="feature-label" style="left:926px; top:1107px;">Motivation</div>
<div class="feature-label" style="left:185px; top:1221px;">Best Results</div>
<div class="feature-label" style="left:926px; top:1224px;">Mind Relaxation</div>

<section class="services">
  <h2 class="section-title">Our Services</h2>
  <div class="service" style="left:119px;">
    <div class="service-icon"><svg width="60" height="50" viewBox="0 0 60 50"><path d="M14 40 C4 38 4 24 12 22 C10 10 24 6 30 12 C36 6 50 10 48 22 C56 24 56 38 46 40 Z M30 12 L30 40" fill="none" stroke="#fff" stroke-width="2"/></svg></div>
    <h3>Brain Fitness</h3>
    <p>eget tempor cursus neque mi con-sectetuer mi a ultricies massa est sed nisl Class aptent taciti socios</p>
  </div>
  <div class="service" style="left:356px;">
    <div class="service-icon"><svg width="60" height="50" viewBox="0 0 60 50"><circle cx="20" cy="22" r="11" fill="none" stroke="#fff" stroke-width="2"/><circle cx="40" cy="22" r="11" fill="none" stroke="#fff" stroke-width="2"/><path d="M12 40 H48" stroke="#fff" stroke-width="2"/></svg></div>
    <h3>Coaching</h3>
    <p>eget tempor cursus neque mi con-sectetuer mi a ultricies massa est sed nisl Class aptent taciti socios</p>
  </div>
  <div class="service" style="left:592px;">
    <div class="service-icon"><svg width="60" height="50" viewBox="0 0 60 50"><g fill="none" stroke="#fff" stroke-width="2"><circle cx="30" cy="25" r="16"/><path d="M22 20 L30 28 L38 18 M30 28 L30 40"/></g><g fill="#fff"><circle cx="22" cy="20" r="2.5"/><circle cx="38" cy="18" r="2.5"/><circle cx="30" cy="28" r="2.5"/></g></svg></div>
    <h3>Intelligence</h3>
    <p>eget tempor cursus neque mi con-sectetuer mi a ultricies massa est sed nisl Class aptent taciti socios</p>
  </div>
  <div class="service" style="left:829px;">
    <div class="service-icon"><svg width="60" height="50" viewBox="0 0 60 50"><g fill="none" stroke="#fff" stroke-width="2"><path d="M18 44 L18 34 C10 30 10 10 28 8 C44 8 48 20 44 28 L46 34 L40 36 L40 44"/><circle cx="30" cy="22" r="6"/></g></svg></div>
    <h3>Training</h3>
    <p>eget tempor cursus neque mi con-sectetuer mi a ultricies massa est sed nisl Class aptent taciti socios</p>
  </div>
</section>

<section class="testimonials" role="img" aria-label="Photo of a relaxed woman in a bright room under a blue tint">
  <h2 class="section-title">Testimonials</h2>
  <svg class="abs" style="left:0; top:0;" width="1200" height="416" viewBox="0 0 1200 416">
    <g fill="none" stroke="#fff" stroke-width="3">
      <path d="M212 206 V147 H272"/>
      <path d="M928 323 H988 V264"/>
      <path d="M122 208 L138 222 L122 236"/>
      <path d="M1078 208 L1062 222 L1078 236"/>
    </g>
  </svg>
  <div class="quote-mark">&#8221;</div>
  <p class="quote-text">" Sed ut perspiciatis unde omnis iste natus error sit voluptatem accusantium doloremque laudantium, totam rem aperiam, eaque ipsa quae ab illo inventore veritatis et quasi architecto beatae vitae dicta sunt explicabo. Nemo enim ipsam voluptatem quia voluptas sit aspernatur</p>
  <div class="quote-author">By Author Name</div>
  <div class="quote-rule"></div>
</section>

<h2 class="section-title blogs-title">Latest Blogs</h2>

<article class="blog-card" style="left:125px; top:2354px; width:472px; height:342px;">
  <div class="blog-media" role="img" aria-label="Glowing profile of a head with light network" style="left:0; top:0; width:470px; height:205px; background:radial-gradient(ellipse at 45% 50%, #4a6e8c 0%, #1a2c40 55%, #0b1118 100%);"></div>
  <h4 style="left:24px; top:222px;">Etiam est nunc venenatis in tristique</h4>
  <p style="left:24px; top:252px; width:400px;">netus et malesuada fames ac turpis egestas Cras id elit Integer quis urna Ut ante enim dapibus malesuada fringilla eu condimen</p>
  <div class="btn-read" style="left:24px; top:290px;">Read More</div>
</article>

<article class="blog-card" style="left:610px; top:2354px; width:474px; height:164px;">
  <div class="blog-media" role="img" aria-label="Photo of a stressed woman holding her head" style="left:0; top:0; width:216px; height:162px; background:linear-gradient(135deg, #e9e6e3 0%, #c9bdb4 55%, #a99a8f 100%);"></div>
  <h4 style="left:240px; top:22px;">Blog Title here</h4>
  <p style="left:240px; top:52px; width:210px;">netus et malesuada fames ac turpis egestas Cras id elit Integer quis urna Ut ante enim dapibus malesua</p>
  <div class="btn-read" style="left:240px; top:114px;">Read More</div>
</article>

<article class="blog-card" style="left:610px; top:2530px; width:474px; height:166px;">
  <div class="blog-media" role="img" aria-label="Photo of a man thinking at a desk" style="left:0; top:0; width:216px; height:164px; background:linear-gradient(135deg, #eef0f2 0%, #c8ccd2 55%, #8c9099 100%);"></div>
  <h4 style="left:240px; top:22px;">Blog Title here</h4>
  <p style="left:240px; top:52px; width:210px;">netus et malesuada fames ac turpis egestas Cras id elit Integer quis urna Ut ante enim dapibus malesua</p>
  <div class="btn-read" style="left:240px; top:116px;">Read More</div>
</article>

<section class="contact" role="img" aria-label="Dark blue abstract digital technology background">
  <h2 class="section-title">Contact Us</h2>
  <div class="contact-rule"></div>
  <div class="contact-info">
    <div class="contact-item">
      <span class="contact-icon"><svg width="16" height="18" viewBox="0 0 16 18"><path d="M8 1 C4 1 2 4 2 7 C2 11 8 17 8 17 C8 17 14 11 14 7 C14 4 12 1 8 1 Z" fill="#fff"/><circle cx="8" cy="7" r="2.4" fill="#a3195b"/></svg></span>
      <span>42 Linden Row, Suite 3, Austin TX 78701</span>
    </div>
    <div class="contact-item">
      <span class="contact-icon"><svg width="16" height="16" viewBox="0 0 16 16"><path d="M3 1 L6 1 L7 5 L5 6.5 C6 9 7 10 9.5 11 L11 9 L15 10 L15 13 C15 14 14 15 13 15 C6 15 1 10 1 3 C1 2 2 1 3 1 Z" fill="#fff"/></svg></span>
      <span>555.014.2290</span>
    </div>
    <div class="contact-item">
      <span class="contact-icon"><svg width="16" height="12" viewBox="0 0 16 12"><rect x="0.5" y="0.5" width="15" height="11" fill="#fff"/><path d="M0.5 0.5 L8 7 L15.5 0.5" fill="none" stroke="#a3195b" stroke-width="1.5"/></svg></span>
      <span>hello@willowcrestmind.com</span>
    </div>
  </div>
  <div class="field" style="left:232px; top:221px; width:344px;">Name</div>
  <div class="field" style="left:585px; top:221px; width:342px;">Email</div>
  <div class="field" style="left:232px; top:271px; width:344px;">Phone</div>
  <div class="field" style="left:585px; top:271px; width:342px;">How did you find us?</div>
  <div class="field field-message" style="left:232px; top:321px; width:695px;">Message</div>
  <div class="btn-submit">Submit Now</div>
</section>

<footer class="site-footer">© 2018 Willow Crest Mind Studio &nbsp;All right reserved. &nbsp;Terms of Use</footer>

</body>
</html>
```